Progressive Architecture and Urban Planning Studio - Stationery Design

The Kestrel Collective: a small boutique Architectural and Urban Planning Studio based in Natal/ RN, Brazil, about to open branches in South Africa and West Africa, established to provide high quality, innovative design and personal client service for projects worldwide. Our approach to Architecture: Minimal - Less is More, so to speak, but with an edge! Strive to produce "clean" projects - stripped of all that can be stripped, no excesses. Got our Logo right here with Pixel Harbor, and hope to do the same with our stationery (were informed that includes business cards, letterhead and envelopes). Since we'll be using two clour schemes, we want at least one using a black background (business card). We'll also allow manipulation of our logo if it helps the final design. Good Luck!

Font styles to use
Other font styles liked:
• Nexa

Colors

Designer to choose colors to be used in the design.

Requirements
Must have
• Business Cards/ Letterheads with the following address:
Rua Olavo Pereira 2741, Vale Dourado, Natal/RN
Should be able to edit it.

```html
<!DOCTYPE html>
<html lang="en">
<head>
<meta charset="utf-8">
<title>The Kestrel Collective – Stationery</title>
<link rel="stylesheet" href="https://fonts.googleapis.com/css2?family=Montserrat:wght@400;600&family=Roboto+Condensed:wght@400;700&display=swap">
<style>
:root{
  --red:#c11c1f;
  --red-dark:#7d0c0f;
  --black:#0b0b0b;
  --white:#ffffff;
  --ink:#222222;
  --grey-light:#d9d9d9;
  --stage-a:#8a8a8a;
  --stage-b:#4a4a4a;
}
*{margin:0;padding:0;box-sizing:border-box}
html,body{width:1200px;height:1000px;overflow:hidden}
body{
  position:relative;
  background:radial-gradient(ellipse at 40% 40%,var(--stage-a),var(--stage-b));
  font-family:"Roboto Condensed",Arial,sans-serif;
  color:var(--ink);
}
.piece{position:absolute;background:var(--white);overflow:hidden}
.wave{position:absolute;left:0;display:block}
.brand{
  display:flex;align-items:center;gap:10px;
  font-family:"Montserrat",Arial,sans-serif;font-weight:400;
  letter-spacing:.28em;text-transform:uppercase;color:var(--black);white-space:nowrap;
}
.brand-square{width:14px;height:14px;background:var(--red);flex:none}
.icon{width:16px;height:16px;background:var(--red);display:inline-flex;align-items:center;justify-content:center;flex:none}
.icon svg{width:11px;height:11px}

/* Letterhead */
.letterhead{left:18px;top:43px;width:643px;height:910px}
.letterhead .brand{position:absolute;left:0;right:0;top:42px;justify-content:center;font-size:19px}
.letterhead .brand-square{width:22px;height:22px}
.contact-row{position:absolute;left:0;right:0;top:86px;display:flex;justify-content:center;gap:16px;font-size:11px;font-weight:700}
.contact-row span{display:flex;align-items:center;gap:6px}
.body-copy{position:absolute;left:29px;top:167px;width:595px;font-size:12.2px;line-height:13px;color:#333}
.body-copy p{margin-bottom:25px}
.signature-mark{position:absolute;left:30px;top:645px;width:85px;height:32px;background:#e8e8e8}
.signer{position:absolute;left:30px;top:693px;line-height:18px}
.signer .name{color:var(--red);font-weight:700;font-size:15px}
.signer .role{font-weight:700;font-size:14px;color:var(--black)}
.footer-address{position:absolute;left:150px;top:880px;display:flex;align-items:center;gap:14px;color:var(--white);font-weight:700;font-size:13px}
.footer-address .icon{background:var(--white);width:20px;height:20px}

/* Business cards */
.card-front{left:709px;top:19px;width:419px;height:268px;background:var(--black)}
.card-front .brand{position:absolute;left:0;right:0;top:103px;justify-content:center;font-size:17px;color:var(--grey-light)}
.card-front .brand-square{background:var(--grey-light);width:20px;height:20px}
.card-back{left:709px;top:303px;width:421px;height:271px}
.card-back .brand{position:absolute;left:11px;top:64px;font-size:14px}
.card-back .brand-square{width:18px;height:18px}
.card-back .person{position:absolute;left:19px;top:120px;line-height:15px}
.card-back .person .name{color:var(--red);font-weight:700;font-size:17px}
.card-back .person .role{font-weight:700;font-size:13px;color:var(--black)}
.card-contacts{position:absolute;left:19px;top:172px;list-style:none;font-weight:700;font-size:13.5px;color:var(--black)}
.card-contacts li{display:flex;gap:9px;align-items:flex-start;margin-bottom:4px;line-height:16px}
.card-contacts .icon{width:19px;height:19px}

/* Envelopes */
.envelope-front{left:687px;top:601px;width:464px;height:179px}
.envelope-front .brand{position:absolute;left:14px;top:20px;font-size:11px}
.address-fields{position:absolute;left:269px;top:58px;font-size:9.5px;font-weight:700;color:var(--black)}
.address-fields div{display:flex;align-items:flex-end;height:17px}
.address-fields label{width:53px}
.address-fields i{display:block;width:85px;border-bottom:1px solid var(--black);margin-bottom:3px}
.envelope-back{left:687px;top:800px;width:466px;height:180px}
.envelope-back .brand{position:absolute;right:12px;bottom:8px;font-size:11px}
</style>
</head>
<body>

<!-- Letterhead -->
<section class="piece letterhead">
  <div class="brand"><span class="brand-square"></span>The Kestrel Collective</div>
  <div class="contact-row">
    <span><i class="icon"><svg viewBox="0 0 12 12"><path d="M3 1l2 2-1 1.5c.7 1.5 2 2.8 3.5 3.5L9 7l2 2-1.5 2C5 10.5 1.5 7 1 2.5z" fill="#fff"/></svg></i>+123 456 7890</span>
    <span><i class="icon"><svg viewBox="0 0 12 12"><rect x="1" y="3" width="10" height="7" fill="#fff"/><path d="M1 3l5 4 5-4" stroke="#c11c1f" fill="none"/></svg></i>YOURNAME@KESTRELMAIL.COM</span>
    <span><i class="icon"><svg viewBox="0 0 12 12"><circle cx="6" cy="6" r="4.5" fill="none" stroke="#fff"/><path d="M1.5 6h9M6 1.5v9" stroke="#fff"/></svg></i>WWW.KESTRELCOLLECTIVE.COM</span>
  </div>
  <div class="body-copy">
    <p>A letterhead is the heading at the top of a sheet of letter paper (stationery). That heading usually consists of a name and an address, and a logo or corporate design, and sometimes a background pattern. The term "letterhead" is often used to refer to the whole sheet imprinted with such a heading.The majority of company letterheads are printed A4 in size (210mm x 297mm) although occasionally A5 (148mm x 210mm) and other bespoke sizes are sometimes used. [citation needed] Certain pieces of information are required to be displayed by law for UK based limited companies. The company name must be included, the place of registration, the registered number and the address of the registered office</p>
    <p>A letterhead is the heading at the top of a sheet of letter paper (stationery). That heading usually consists of a name and an address, and a logo or corporate design, and sometimes a background pattern. The term "letterhead" is often used to refer to the whole sheet imprinted with such a heading.The majority of company letterheads are printed A4 in size (210mm x 297mm) although occasionally A5 (148mm x 210mm) and other bespoke sizes are sometimes used. [citation needed] Certain pieces of information are required to be displayed by law for UK based limited companies. The company name must be included, the place of registration, the registered number and the address of the registered office</p>
    <p>A letterhead is the heading at the top of a sheet of letter paper (stationery). That heading usually consists of a name and an address, and a logo or corporate design, and sometimes a background pattern. The term "letterhead" is often used to refer to the whole sheet imprinted with such a heading.The majority of company letterheads are printed A4 in size (210mm x 297mm) although occasionally A5 (148mm x 210mm) and other bespoke sizes are sometimes used. [citation needed] Certain pieces of information are required to be displayed by law for UK based limited companies. The company name must be included, the place of registration, the registered number and the address of the registered office</p>
    <p>A letterhead is the heading at the top of a sheet of letter paper (stationery). That heading usually consists of a name and an address, and a logo or corporate design, and sometimes a background pattern. The term "letterhead" is often used to refer to the whole sheet imprinted with such a heading.The majority of company letterheads are printed A4 in size (210mm x 297mm) although occasionally A5 (148mm x 210mm) and other bespoke sizes are sometimes used. [citation needed] Certain pieces of information are required to be displayed by law for UK based limited companies. The company name must be included, the place of registration, the registered number and the address of the registered office</p>
  </div>
  <div class="signature-mark" role="img" aria-label="Handwritten signature"></div>
  <div class="signer"><div class="name">YOUR NAME</div><div class="role">OWNER</div></div>
  <svg class="wave" style="top:808px" width="643" height="102" viewBox="0 0 643 102" preserveAspectRatio="none">
    <defs><linearGradient id="lhRed" x1="0" y1="0" x2="0" y2="1"><stop offset="0" stop-color="#c11c1f"/><stop offset="1" stop-color="#7d0c0f"/></linearGradient></defs>
    <path d="M0 15 Q330 60 643 0 L643 102 L0 102Z" fill="#0b0b0b"/>
    <path d="M0 30 Q330 56 643 18 L643 102 L0 102Z" fill="url(#lhRed)"/>
  </svg>
  <div class="footer-address">
    <i class="icon"><svg viewBox="0 0 12 12"><path d="M6 1.5L1 6h1.5v4.5h7V6H11z" fill="#c11c1f"/></svg></i>
    RUA OLAVO PEREIRA 2741, VALE DOURADO, NATAL/RN
  </div>
</section>

<!-- Business card, black side -->
<section class="piece card-front">
  <div class="brand"><span class="brand-square"></span>The Kestrel Collective</div>
  <svg class="wave" style="top:160px" width="419" height="108" viewBox="0 0 419 108" preserveAspectRatio="none">
    <defs><linearGradient id="cfRed" x1="0" y1="0" x2="0" y2="1"><stop offset="0" stop-color="#c11c1f"/><stop offset="1" stop-color="#7d0c0f"/></linearGradient></defs>
    <path d="M0 20 Q160 70 419 10 L419 108 L0 108Z" fill="#fff"/>
    <path d="M0 30 Q170 72 419 30 L419 108 L0 108Z" fill="url(#cfRed)"/>
  </svg>
</section>

<!-- Business card, white side -->
<section class="piece card-back">
  <svg class="wave" style="top:0" width="421" height="90" viewBox="0 0 421 90" preserveAspectRatio="none">
    <defs><linearGradient id="cbRed" x1="0" y1="0" x2="0" y2="1"><stop offset="0" stop-color="#9a1215"/><stop offset="1" stop-color="#c11c1f"/></linearGradient></defs>
    <path d="M0 0 H421 V90 Q250 20 0 28Z" fill="#0b0b0b"/>
    <path d="M0 0 H421 V68 Q250 12 0 22Z" fill="url(#cbRed)"/>
  </svg>
  <div class="brand"><span class="brand-square"></span>The Kestrel Collective</div>
  <div class="person"><div class="name">YOUR NAME</div><div class="role">OWNER</div></div>
  <ul class="card-contacts">
    <li><i class="icon"><svg viewBox="0 0 12 12"><path d="M3 1l2 2-1 1.5c.7 1.5 2 2.8 3.5 3.5L9 7l2 2-1.5 2C5 10.5 1.5 7 1 2.5z" fill="#fff"/></svg></i>+123 456 7890</li>
    <li><i class="icon"><svg viewBox="0 0 12 12"><rect x="1" y="3" width="10" height="7" fill="#fff"/><path d="M1 3l5 4 5-4" stroke="#c11c1f" fill="none"/></svg></i>YOURNAME@KESTRELMAIL.COM</li>
    <li><i class="icon"><svg viewBox="0 0 12 12"><circle cx="6" cy="6" r="4.5" fill="none" stroke="#fff"/><path d="M1.5 6h9M6 1.5v9" stroke="#fff"/></svg></i>WWW.KESTRELCOLLECTIVE.COM</li>
    <li><i class="icon"><svg viewBox="0 0 12 12"><path d="M6 1.5L1 6h1.5v4.5h7V6H11z" fill="#fff"/></svg></i>RUA OLAVO PEREIRA 2741, VALE DOURADO,<br>NATAL/RN</li>
  </ul>
</section>

<!-- Envelope, front -->
<section class="piece envelope-front">
  <div class="brand"><span class="brand-square"></span>The Kestrel Collective</div>
  <div class="address-fields">
    <div><label>RECEPIENT:</label><i></i></div>
    <div><label>ADDRESS:</label><i></i></div>
    <div><label>CITY:</label><i></i></div>
    <div><label>COUNTRY:</label><i></i></div>
  </div>
  <svg class="wave" style="top:135px" width="464" height="44" viewBox="0 0 464 44" preserveAspectRatio="none">
    <defs><linearGradient id="efRed" x1="0" y1="0" x2="0" y2="1"><stop offset="0" stop-color="#c11c1f"/><stop offset="1" stop-color="#7d0c0f"/></linearGradient></defs>
    <path d="M0 10 Q230 22 464 2 L464 44 L0 44Z" fill="#0b0b0b"/>
    <path d="M0 17 Q230 24 464 9 L464 44 L0 44Z" fill="url(#efRed)"/>
  </svg>
</section>

<!-- Envelope, back -->
<section class="piece envelope-back">
  <svg class="wave" style="top:0" width="466" height="85" viewBox="0 0 466 85">
    <defs><linearGradient id="ebRed" x1="0" y1="0" x2="0" y2="1"><stop offset="0" stop-color="#9a1215"/><stop offset="1" stop-color="#c11c1f"/></linearGradient></defs>
    <path d="M0 0 H466 L265 76 Q233 84 200 76Z" fill="url(#ebRed)"/>
  </svg>
  <div class="brand"><span class="brand-square"></span>The Kestrel Collective</div>
</section>

</body>
</html>
```